Business cards for Home & Garden Design business
Oakvale Grove Design
Business cards for Home & Garden Design business - Home and Garden
Creative Brief
Bright & Fun-filled
Marla Pendby
Designer
PO Box 732 Winkler, MB R6W 2K9
marlapendby@oakvalegrovedesign.example
oakvalegrovedesign.example
Would love to have my logo on a background of a rustic, white fence/door, or white birch trees. Question - do you already have access to my logo, or how do I upload it?

```html
<!DOCTYPE html>
<html lang="en">
<head>
<meta charset="utf-8">
<title>Oakvale Grove Design – Business Cards</title>
<link href="https://fonts.googleapis.com/css2?family=Montserrat:wght@400;500;600&display=swap" rel="stylesheet">
<style>
  :root {
    --page: #e9e9eb;
    --card-dark: #24252b;
    --card-light: #ffffff;
    --teal: #4fa7ad;
    --ink: #2a2b30;
    --muted: #6b6d74;
    --soft: #c9cace;
  }
  * { box-sizing: border-box; margin: 0; padding: 0; }
  html, body { width: 1200px; height: 878px; overflow: hidden; }
  body {
    background: var(--page);
    font-family: "Montserrat", Arial, sans-serif;
    position: relative;
  }
  .card {
    position: absolute;
    top: 290px;
    width: 520px;
    height: 298px;
    border-radius: 18px;
    overflow: hidden;
    box-shadow: 0 10px 28px rgba(0,0,0,0.18);
  }
  .card-back { left: 60px; background: var(--card-dark); }
  .card-front { left: 620px; background: var(--card-light); }

  .brand {
    position: absolute;
    display: flex;
    align-items: center;
    gap: 10px;
    font-weight: 500;
    letter-spacing: 0.5px;
    white-space: nowrap;
  }
  .brand-dot { width: 18px; height: 18px; border-radius: 50%; flex: none; }
  .card-back .brand { left: 0; right: 0; top: 112px; justify-content: center; font-size: 26px; color: var(--teal); }
  .card-back .brand-dot { background: var(--teal); }
  .website {
    position: absolute; left: 0; right: 0; top: 196px;
    text-align: center; color: #ffffff; font-size: 13px; letter-spacing: 0.6px;
  }

  .card-front .brand { right: 38px; top: 92px; font-size: 22px; color: var(--ink); }
  .card-front .brand-dot { background: var(--teal); }

  .side-strip { position: absolute; left: 0; top: 0; width: 100%; height: 100%; }
  .contact {
    position: absolute; left: 44px; top: 136px;
    color: var(--muted); font-size: 9.5px; line-height: 1.55;
    white-space: nowrap;
  }
  .contact .name { color: var(--teal); font-size: 16px; font-weight: 500; line-height: 1.2; }
  .contact .role { color: var(--ink); font-size: 10px; margin-bottom: 12px; }
  .contact .address { margin-bottom: 10px; }
</style>
</head>
<body>
  <section class="card card-back">
    <div class="brand"><span class="brand-dot"></span>Oakvale Grove Design</div>
    <p class="website">www.oakvalegrovedesign.example</p>
  </section>

  <section class="card card-front">
    <svg class="side-strip" viewBox="0 0 520 298" aria-hidden="true">
      <path d="M0 180 L24 180 L24 298 L0 298 Z" fill="#24252b"/>
      <path d="M0 240 Q60 250 90 298 L0 298 Z" fill="#24252b"/>
      <g fill="none" stroke="#ffffff" stroke-width="1.2">
        <circle cx="12" cy="196" r="4.5"/>
        <circle cx="12" cy="215" r="4.5"/>
        <circle cx="12" cy="234" r="4.5"/>
        <circle cx="12" cy="253" r="4.5"/>
      </g>
      <g stroke="#c9cace" stroke-width="2">
        <line x1="50" y1="285" x2="58" y2="273"/>
        <line x1="58" y1="285" x2="66" y2="273"/>
        <line x1="66" y1="285" x2="74" y2="273"/>
      </g>
    </svg>
    <div class="brand"><span class="brand-dot"></span>Oakvale Grove Design</div>
    <div class="contact">
      <p class="name">Marla Pendby</p>
      <p class="role">General Manager</p>
      <p class="address">42 Fernlow Row Mall,<br>Brindlemoor, Avel, QX</p>
      <p>P: 555 018 2741</p>
      <p>F: 555 018 2742</p>
      <p>marlapendby@oakvalegrovedesign.example</p>
    </div>
  </section>
</body>
</html>
```